依頼詳細
海の家で開催するアコーステックライブのフライヤーです。

カフェやBarなど店舗に配布します。
開催まで日が少ないため早めに提案頂ける方、宜しくお願いします。

さわやか、ナチュラル、上品、20代~30代女性向け、オシャレな感じ

インスタグラム https://www.instagram.com/k72.note/
FB https://www.facebook.com/sunnyreefhut/

インスタやFBを見ていただき、雰囲気やテイストをイメージしていただければ幸いです。写真も必要であれば使ってください。

潮風の言葉に引っ張られず、自由にデザイン頂きたいです。
記載項目
開催概要
タイトル/潮風芸能祭Autumn Gala
日付/2016/09/11(SUN)
時間/OPEN/16:30 START/17:00 END/20:00
会場/海の家Sunny Reef Hut(佐賀県唐津市潮見町海水浴場)
LIVE/dawnrow/KORUE/MINT RIVER with WABELUK
TICKET/前売¥3,000- 当日¥4,000- 1Drink付
予約方法/①開催日 ②氏名 ③人数 ④連絡先電話番号をお伝えください。
連絡先/TEL080-7010-6213 MAIL info@sunnyreefhut.example

アーティスト情報は添付資料参照ください
サイズ
B6
ページ数
両面
希望イメージ
シンプル 複雑
単色 カラフル
暗い 明るい
日常 高級
遊び心 厳粛
未来的 伝統的
女性的 男性的
希望する色
納品ファイル
• 高解像度JPG (.jpg)
• イラストレーター形式 (.ai)
補足説明
■ 選んだ理由

スタッフの皆で協議の結果選定させていただきました。
ありがとうございました。

■ 提案者全員のお礼・コメント

今回ご提案いただきました皆様、どのデザインも良く、自分たちのイメージに沿った提案をいただき、選定に悩みました。
提案いただき本当にありがとうございました!
今後も機会があれば宜しくお願いします

```html
<!DOCTYPE html>
<html lang="ja">
<head>
<meta charset="utf-8">
<title>潮風芸能祭 Autumn Gala</title>
<link rel="stylesheet" href="https://fonts.googleapis.com/css2?family=Noto+Sans+JP:wght@400;500;700&family=Lato:wght@400;700&display=swap">
<style>
  :root {
    --sky-top: #8e97ab;
    --sky-mid: #c9b3ad;
    --horizon: #eab483;
    --sea: #b99786;
    --deck-light: #6b4b38;
    --deck-dark: #241812;
    --ink: #ffffff;
    --shadow: rgba(40, 25, 15, 0.45);
  }
  html, body {
    margin: 0;
    padding: 0;
    width: 845px;
    height: 1200px;
    overflow: hidden;
    background: #ffffff;
  }
  .flyer {
    position: relative;
    width: 845px;
    height: 1200px;
    overflow: hidden;
    color: var(--ink);
    font-family: "Noto Sans JP", sans-serif;
    text-shadow: 0 1px 4px var(--shadow);
  }
  .scene-photo {
    position: absolute;
    inset: 0;
    background: linear-gradient(180deg,
      var(--sky-top) 0%,
      var(--sky-mid) 18%,
      var(--horizon) 34%,
      var(--sea) 42%,
      var(--deck-light) 58%,
      var(--deck-dark) 100%);
  }
  .title {
    position: absolute;
    left: 415px;
    top: 415px;
    margin: 0;
    font-size: 64px;
    font-weight: 500;
    letter-spacing: 2px;
    line-height: 1;
  }
  .subtitle {
    position: absolute;
    left: 418px;
    top: 548px;
    margin: 0;
    font-family: "Lato", sans-serif;
    font-size: 36px;
    font-weight: 400;
    font-variant: small-caps;
    letter-spacing: 3px;
    line-height: 1;
  }
  .schedule {
    position: absolute;
    left: 105px;
    top: 632px;
    font-size: 31px;
    font-weight: 500;
    line-height: 1.6;
  }
  .schedule .date { margin: 0; }
  .schedule .time { margin: 0 0 0 34px; }
  .venue {
    position: absolute;
    left: 152px;
    top: 930px;
    font-size: 31px;
    font-weight: 500;
  }
  .venue .name { margin: 0; }
  .venue .name .latin {
    font-family: "Lato", sans-serif;
    font-variant: small-caps;
    letter-spacing: 2px;
    margin-left: 10px;
  }
  .venue .address {
    margin: 8px 0 0 158px;
    font-size: 22px;
    font-weight: 400;
    letter-spacing: 1px;
  }
  .host-mark {
    position: absolute;
    left: 716px;
    top: 1066px;
    width: 102px;
    height: 102px;
    background: #2f2620;
    display: flex;
    align-items: center;
    justify-content: center;
    text-align: center;
    font-family: "Lato", sans-serif;
    font-size: 15px;
    font-weight: 400;
    line-height: 1.3;
    text-shadow: none;
  }
</style>
</head>
<body>
  <main class="flyer">
    <div class="scene-photo" role="img" aria-label="夕暮れの海辺、海の家のウッドデッキと木組みのパラソル越しに見える夕焼けの空と海"></div>

    <h1 class="title">潮風芸能祭</h1>
    <p class="subtitle">Autumn Gala</p>

    <section class="schedule">
      <p class="date">日時 2016/09/11（SUN）</p>
      <p class="time">OPEN/16：30</p>
      <p class="time">START/17：00</p>
    </section>

    <section class="venue">
      <p class="name">会場　海の家<span class="latin">Sunny Reef Hut</span></p>
      <p class="address">佐賀県唐津市潮見町海水浴場</p>
    </section>

    <div class="host-mark">Sunny<br>Reef Hut</div>
  </main>
</body>
</html>
```